Video Thumbnail Design for Jazz Piano YouTube channel

Hello, my name’s Marcus Fenwick. I run a jazz piano YouTube channel called ‘Keyset Lessons’ (www.vidloop-example.com/keysetlessons). It’s the most subscribed to jazz piano YouTube channel with over 200,000 subscribers.

I need a designer to create an eye-catching thumbnail, to be used for my upcoming videos.

BRIEF:
For now, I’m asking for just one thumbnail design. I will choose a designer from this initial project, and I plan to commission additional designs from the same designer - so that my thumbnails all have a coherent look.

WHAT MAKES A GOOD THUMBNAIL:
Above all, your thumbnail design must be EYE-CATCHING and STAND OUT. Imagine scrolling through hundreds of YouTube videos - the video’s thumbnail artwork is one of the key aspects that gets someone to click and watch a video, so this is a VERY important aspect to getting views.

Your design can be innovative - surprise me. I want your design to JUMP OUT at me. For example, you could experiment with creating a 3D effect, or having elements popping out of the frame. A YouTube thumbnail doesn’t have to be square to the edges - you can add white around the edges to create an unusual jagged effect (when viewed in YouTube's search, which has a white background), and certain things could come out of the picture (see attached files for reference).

Remember, YouTube thumbnails are displayed very small - especially on desktop. It’s a good idea to design your thumbnail at this small size, rather than at full size on your computer screen. You'll probably need to zoom in closer to my face and enlarge the text more than you normally would if you were creating a larger image.

Lots of contrast is needed in a tiny thumbnail. Blacks must be pitch black, whites must be white, color saturation - the thumbnail must contain a lot of energy in a small space.

A strong format for YouTube thumbnails is to have a FACE (my face) and TEXT (large white text, 3 - 5 words). You can use this if you like, or you can experiment with a different format. I’m completely open to your ideas.

BRAND LOOK & FEEL:
Here are some keywords that describe my brand:
- Calm
- Professional
- Sophisticated (jazz is a sophisticated style of music)
View my channel to see my visual style as a starting point: www.vidloop-example.com/keysetlessons

BRAND COLORS:
- Turquoise: Hex #00DBD7 (this is my main brand color and must be used in the thumbnail)
- Black
- White
- Red: #FC5B5B (I sometimes use this as a secondary color - you can use this in your design if you want, or not).

TEXT:
The font I use for my brand is ‘Lovelo’ (please use this font in your design - included in my attachment).
I like my text to be white against a black background.
For your design, you could use the text: 'SWEET CHORD VOICING' as sample text.

IMAGES:
I've attached several photos for you to work with - just choose one for your design. The backgrounds are not important to the Thumbnail - only me and the piano are needed - so it's up to you whether you black out the background, darken it, or leave it in. Feel free to zoom in, rotate at an angle, distort, etc.

SLANTS:
I like diagonal lines and slants - because they go well with the ‘jazz’ feel. This could include the text itself (at an angle instead of straight), or the picture (any images of me or the piano could be at an angle, rather than straight).

DIMENSIONS:
YouTube thumbnails must be 1280 pixels wide by 720 pixels tall. A ratio of 16:9 is ideal as it’s used most often in YouTube players and previews.

DELIVERABLES:
If your design is selected - I will need a Photoshop file delivered of the final design (this is so that I can edit the text myself to make it relevant to the video).

After that, I will commission further designs with you (these will be separate projects, each with its own payment). My end goal is to have 10 - 15 strong thumbnail designs - all from the same designer.

Thank you very much for your submission, I can't wait to see what you come up with!

Target Market(s)

My audience is 90% male, between 25 - 65 years old. I have viewers worldwide, but they mostly live in the US and Canada.

Font styles to use
Other font styles liked:
• Lovelo

Colors
31b7a3

Requirements
Must have
• Image and text (as described in the project description)
Nice to have
• Creative use of white edges to stand out on YouTube (against other traditional square looking thumbnails).
• See full description in the project description.

```html
<!DOCTYPE html>
<html lang="en">
<head>
<meta charset="utf-8">
<title>Sweet Chord Voicing – Thumbnail</title>
<link rel="stylesheet" href="https://fonts.googleapis.com/css2?family=League+Spartan:wght@800&display=swap">
<style>
  :root {
    --page: #ffffff;
    --frame-yellow: #e8e512;
    --frame-black: #0a0a0a;
    --sky-light: #0fb2dc;
    --sky-deep: #0b6db4;
    --line-cream: #f3f1c8;
    --white: #ffffff;
    --title-stroke: #ee4f2b;
    --photo-light: #a9dccd;
    --photo-dark: #1c1c1c;
  }
  html, body {
    margin: 0;
    width: 1200px;
    height: 1000px;
    overflow: hidden;
    background: var(--page);
  }
  .thumbnail {
    display: block;
    width: 1200px;
    height: 1000px;
  }
  .title-line {
    font-family: "League Spartan", sans-serif;
    font-weight: 800;
    font-size: 72px;
    fill: var(--white);
    stroke: var(--title-stroke);
    stroke-width: 9px;
    stroke-linejoin: round;
    paint-order: stroke fill;
  }
  .deco-line { stroke: var(--line-cream); stroke-width: 5; stroke-linecap: round; }
  .thin-white { stroke: var(--white); fill: none; }
  .bars line { stroke: var(--white); stroke-width: 3; stroke-linecap: round; }
</style>
</head>
<body>
<svg class="thumbnail" viewBox="0 0 1200 1000" xmlns="http://www.w3.org/2000/svg">
  <defs>
    <linearGradient id="sky" x1="0" y1="0" x2="1" y2="0.3">
      <stop offset="0" stop-color="var(--sky-light)"/>
      <stop offset="0.6" stop-color="#0a93cf"/>
      <stop offset="1" stop-color="var(--sky-deep)"/>
    </linearGradient>
    <linearGradient id="photo-tone" x1="0" y1="0" x2="1" y2="1">
      <stop offset="0" stop-color="var(--photo-light)"/>
      <stop offset="0.6" stop-color="#7fb8ad"/>
      <stop offset="1" stop-color="var(--photo-dark)"/>
    </linearGradient>
    <clipPath id="panel-clip">
      <polygon points="130,213 1117,213 1070,760 88,760"/>
    </clipPath>
  </defs>

  <g class="frame">
    <polygon points="122,203 1137,203 1083,772 70,772" fill="var(--frame-yellow)"/>
    <polygon points="122,203 450,203 450,214 132,214 115,410 103,410" fill="var(--frame-black)"/>
    <polygon points="1100,590 1083,772 760,772 760,760 1070,760 1085,590" fill="var(--frame-black)"/>
  </g>

  <g class="panel" clip-path="url(#panel-clip)">
    <polygon points="130,213 1117,213 1070,760 88,760" fill="url(#sky)"/>
    <path d="M1010 213 C1060 330 980 420 1030 540 C1060 610 1110 600 1120 590 L1120 213 Z" fill="#0c67ae" opacity="0.6"/>

    <line class="deco-line" x1="260" y1="325" x2="372" y2="215"/>
    <line class="deco-line" x1="400" y1="560" x2="700" y2="262"/>
    <line class="deco-line" x1="770" y1="597" x2="840" y2="528"/>
    <line class="deco-line" x1="880" y1="650" x2="1100" y2="430"/>

    <circle cx="534" cy="255" r="49" fill="var(--white)"/>
    <circle cx="534" cy="255" r="20" fill="#0a8fcf"/>
    <circle cx="534" cy="255" r="10" fill="var(--white)"/>

    <circle cx="1061" cy="522" r="23" fill="var(--white)"/>
    <circle cx="1061" cy="522" r="10" fill="#0a8fcf"/>
    <circle cx="1061" cy="522" r="5" fill="var(--white)"/>

    <g class="thin-white" stroke-width="2">
      <circle cx="230" cy="323" r="23"/>
      <circle cx="230" cy="323" r="13"/>
      <circle cx="230" cy="323" r="5"/>
    </g>

    <g class="bars">
      <line x1="145" y1="222" x2="145" y2="230"/><line x1="153" y1="218" x2="153" y2="234"/>
      <line x1="161" y1="215" x2="161" y2="237"/><line x1="169" y1="219" x2="169" y2="233"/>
      <line x1="177" y1="215" x2="177" y2="237"/><line x1="185" y1="220" x2="185" y2="232"/>
      <line x1="888" y1="299" x2="888" y2="309"/><line x1="896" y1="294" x2="896" y2="314"/>
      <line x1="904" y1="290" x2="904" y2="318"/><line x1="912" y1="294" x2="912" y2="314"/>
      <line x1="920" y1="299" x2="920" y2="309"/>
      <line x1="982" y1="712" x2="982" y2="724"/><line x1="994" y1="700" x2="994" y2="736"/>
      <line x1="1006" y1="690" x2="1006" y2="746"/><line x1="1018" y1="686" x2="1018" y2="750"/>
      <line x1="1030" y1="694" x2="1030" y2="742"/><line x1="1042" y1="704" x2="1042" y2="732"/>
      <line x1="1054" y1="698" x2="1054" y2="738"/><line x1="1066" y1="712" x2="1066" y2="724"/>
    </g>

    <g class="note" fill="var(--white)">
      <ellipse cx="1000" cy="368" rx="11" ry="8" transform="rotate(-20 1000 368)"/>
      <rect x="1007" y="326" width="4" height="42"/>
      <path d="M1011 326 C1022 336 1038 342 1030 362 C1032 348 1022 344 1011 340 Z"/>
    </g>
  </g>

  <rect class="photo-area" role="img"
        aria-label="Photo of the presenter in a mint shirt playing a black keyboard"
        x="140" y="250" width="340" height="510" rx="6"
        fill="url(#photo-tone)" stroke="var(--white)" stroke-width="6"/>

  <g class="title-box">
    <rect x="598" y="252" width="312" height="338" fill="none" stroke="var(--white)" stroke-width="4"/>
    <path d="M609 296 V264 H640" class="thin-white" stroke-width="4"/>
    <path d="M899 548 V579 H868" class="thin-white" stroke-width="4"/>
    <text class="title-line" x="624" y="372" textLength="194" lengthAdjust="spacingAndGlyphs">SWEET</text>
    <text class="title-line" x="626" y="452" textLength="222" lengthAdjust="spacingAndGlyphs">CHORD</text>
    <text class="title-line" x="626" y="530" textLength="262" lengthAdjust="spacingAndGlyphs">VOICING</text>
  </g>
</svg>
</body>
</html>
```